business card for real estate company

I need a sharp creative business card design that stands out for a real estate company that does the following
- Selling land
- Selling houses and apartments
- Property management

website www.velmoreestates.example
email: info at the above web address
phone number place holder

```html
<!DOCTYPE html>
<html lang="en">
<head>
<meta charset="utf-8">
<title>Velmore Estates – Business Card</title>
<link rel="stylesheet" href="https://fonts.googleapis.com/css2?family=Lato:wght@400;700&family=Roboto:wght@500&display=swap">
<style>
  :root {
    --page-bg: #efefef;
    --card-dark: #0f1524;
    --card-light: #ffffff;
    --brand-green: #5cb646;
    --brand-navy: #1f3364;
    --text-light: #e6e8ee;
    --text-soft: #c9ccd6;
  }
  * { margin: 0; padding: 0; box-sizing: border-box; }
  html, body {
    width: 1200px; height: 1200px; overflow: hidden;
    background: var(--page-bg);
    font-family: "Lato", sans-serif;
  }
  .canvas { position: relative; width: 1200px; height: 1200px; }

  .card {
    position: absolute; left: 283px; width: 633px; height: 361px;
    border-radius: 20px; overflow: hidden;
  }
  .card--front { top: 172px; background: var(--card-dark); }
  .card--back { top: 643px; display: flex; }

  /* wordmark */
  .wordmark {
    display: flex; align-items: center; gap: 12px;
    font-family: "Lato", sans-serif; font-weight: 700;
    font-size: 44px; letter-spacing: 1px; line-height: 1; white-space: nowrap;
  }
  .wordmark__square { width: 15px; height: 15px; background: var(--brand-green); flex: none; }
  .card--front .wordmark {
    position: absolute; right: 63px; top: 130px; color: var(--card-light);
  }

  .services {
    position: absolute; left: 24px; top: 259px; list-style: none;
    font-family: "Roboto", sans-serif; font-weight: 500; font-size: 18px;
    color: var(--brand-green);
  }
  .services li { display: flex; align-items: center; gap: 8px; height: 28px; }
  .services svg { width: 18px; height: 18px; flex: none; }

  /* back */
  .back__brand {
    width: 306px; height: 100%; background: var(--card-light);
    display: flex; align-items: center; justify-content: center;
  }
  .back__brand .wordmark { color: var(--brand-navy); font-size: 30px; gap: 8px; letter-spacing: 0.5px; }
  .back__brand .wordmark__square { width: 11px; height: 11px; }

  .back__details { flex: 1; background: var(--card-dark); padding: 88px 0 0 35px; }
  .person__name { font-weight: 700; font-size: 32px; color: var(--brand-green); line-height: 1.1; }
  .person__role { font-weight: 700; font-size: 17px; color: var(--text-light); margin-top: 4px; }
  .contacts { list-style: none; margin-top: 14px; font-size: 19px; color: var(--text-soft); }
  .contacts li { display: flex; align-items: center; gap: 14px; height: 27.5px; }
  .contacts svg { width: 14px; height: 14px; flex: none; fill: none; stroke: var(--text-soft); stroke-width: 2; }
</style>
</head>
<body>
<div class="canvas">

  <section class="card card--front">
    <div class="wordmark"><span class="wordmark__square"></span>Velmore Estates</div>
    <ul class="services">
      <li><svg viewBox="0 0 18 18"><circle cx="9" cy="9" r="7.5" fill="none" stroke="currentColor" stroke-width="1.5"/><path d="M5.5 9.2l2.4 2.3 4.6-4.8" fill="none" stroke="currentColor" stroke-width="1.6"/></svg>Selling Land</li>
      <li><svg viewBox="0 0 18 18"><circle cx="9" cy="9" r="7.5" fill="none" stroke="currentColor" stroke-width="1.5"/><path d="M5.5 9.2l2.4 2.3 4.6-4.8" fill="none" stroke="currentColor" stroke-width="1.6"/></svg>Property Management</li>
      <li><svg viewBox="0 0 18 18"><circle cx="9" cy="9" r="7.5" fill="none" stroke="currentColor" stroke-width="1.5"/><path d="M5.5 9.2l2.4 2.3 4.6-4.8" fill="none" stroke="currentColor" stroke-width="1.6"/></svg>Selling Houses and Apartments</li>
    </ul>
  </section>

  <section class="card card--back">
    <div class="back__brand">
      <div class="wordmark"><span class="wordmark__square"></span>Velmore Estates</div>
    </div>
    <div class="back__details">
      <p class="person__name">Daniel Mwangi</p>
      <p class="person__role">Founder</p>
      <ul class="contacts">
        <li><svg viewBox="0 0 14 14"><rect x="3.5" y="1" width="7" height="12" rx="1.5"/></svg>+254 700 123 456</li>
        <li><svg viewBox="0 0 14 14"><path d="M1 6.5L13 1 8 13 6.5 8z" fill="var(--text-soft)" stroke="none"/></svg>info@velmoreestates.example</li>
        <li><svg viewBox="0 0 14 14"><circle cx="7" cy="7" r="6"/><path d="M1 7h12M7 1c-3 3.5-3 8.5 0 12M7 1c3 3.5 3 8.5 0 12"/></svg>www.velmoreestates.example</li>
        <li><svg viewBox="0 0 14 14"><path d="M7 13S2.5 8 2.5 5.2a4.5 4.5 0 0 1 9 0C11.5 8 7 13 7 13z" fill="var(--text-soft)" stroke="none"/><circle cx="7" cy="5.2" r="1.6" fill="var(--card-dark)" stroke="none"/></svg>Nairobi, Kenya</li>
      </ul>
    </div>
  </section>

</div>
</body>
</html>
```